Velmarone Website Redesign

We need a redesign of the company website.

We're a company, based in the UK, called Velmarone. We develop software for the Healthcare Industry, used by medical professionals throughout the UK on a daily basis.

We have a suite of tools that form the Velmarone Platform, and all are web-based.

We want to communicate that our software is not only innovative but is the best available, easy to use, and provides exceptional quality and RoI.

Additionally, we want our existing customers to be able to see what else we can offer them.

A site map is attached.
Updates

Hi Everyone,

As we approach the deadline for submissions, we’ve shortlisted threedesigns that we felt were the best of the submissions and have asked thedesigners to make some additional changes and produce some content pages so wecan see what’s beneath the Home page in the rest of the site.

Thank you all for your submissions – there was an awful lot ofdisagreement among everyone here over which designs we thought were best andsome of those that haven’t made it into the final three were very well liked.

Those in the final three have been messaged individually and have theirdesigns as the only non-eliminated ones showing. We would ask at this stagethat anyone not in the final three please do no further work or submitadditional designs as we are approaching the deadline and will not be able toprovide sufficient feedback to allow any changes in a short space of time.

Kind regards,
The Velmarone Team

Target Market(s)

Nurses and medical professionals in western-speaking countries, most notably in the UK.

Predominantly, we expect it will be senior medical staff that will be viewing (and using) our website - some will be existing customers and some will be new or potential customers.

Industry/Entity Type

Medical

Requirements
Must have
• Area to showcase and provide information about products.
• Company information - who we are and why you should choose us.
• News and events - blog, archive newsletters, publications, etc.
• Support section for existing customers - FAQ, Forum, Manuals.
• Contact page.
• We also feel that we'd like to have our telephone number and primary email address visible at all times, with an immediate ability for users to request a demonstration.
Nice to have
• A "My Velmarone" area would be nice at some point, though that's something for further down the line.

```html
<!DOCTYPE html>
<html lang="en">
<head>
<meta charset="utf-8">
<title>Velmarone – Home</title>
<link href="https://fonts.googleapis.com/css2?family=Roboto:wght@300;400;700&display=swap" rel="stylesheet">
<style>
:root{
  --blue:#1a8ee6;
  --ink:#1e1e1e;
  --nav:#1c1c1c;
  --top:#000;
  --band:#ececec;
  --band-dark:#dedede;
  --panel-1:#c9c9c9;
  --panel-2:#bdbdbd;
  --panel-3:#b0b0b0;
  --teal:#3aa9c9;
}
*{margin:0;padding:0;box-sizing:border-box}
html,body{width:955px;height:1200px;overflow:hidden}
body{position:relative;font-family:"Roboto",Arial,sans-serif;color:var(--ink);
  background:linear-gradient(#fafafa 0,#f6f6f6 325px,var(--band) 325px,var(--band) 1062px,var(--band-dark) 1062px,var(--band-dark) 1200px)}
.abs{position:absolute}
.top-strip{left:0;top:0;width:955px;height:23px;background:var(--top)}
.main-nav{left:0;top:23px;width:955px;height:45px;background:var(--nav)}
.main-nav a{position:absolute;top:0;height:45px;line-height:45px;color:#fff;text-decoration:none;font-size:14px;letter-spacing:.2px}
.main-nav a.current{background:#fafafa;color:#222;width:97px;text-align:center;left:54px}
.nav-sep{position:absolute;top:12px;height:12px;border-left:1px dotted #777}
.rss{left:857px;top:32px;width:18px;height:18px;border-radius:3px;background:linear-gradient(#ffb347,#f07b12)}
.brand{left:44px;top:115px;font-size:37px;font-weight:700;color:var(--blue);letter-spacing:-.5px}
.contact{right:42px;top:86px;text-align:right;font-size:11.5px;line-height:13.6px;color:#333}
.contact b{color:var(--blue)}
.contact .k{color:var(--blue)}
.contact .gap{display:block;height:14px}
.content{left:36px;top:210px;width:884px;height:912px;background:#fff;border:1px solid #e6e6e6}
.hero-photo{left:53px;top:236px;width:584px;height:249px;background:linear-gradient(100deg,#cfd3d6,#f2f2f2 45%,#e5e7e9 70%,#9da1a4)}
.replay{left:63px;top:461px;width:56px;height:16px;background:var(--teal);color:#fff;font-size:10px;font-weight:700;text-align:center;line-height:16px}
.quick{left:637px;width:266px;display:flex;align-items:center}
.quick .ico{width:58px;height:58px;margin-left:13px;border-radius:8px;border:2px solid #e8f4fa;background:linear-gradient(135deg,#bfe6f5,#3aa0d6);box-shadow:0 1px 3px rgba(0,0,0,.25)}
.quick span{margin-left:11px;font-size:22px;font-weight:700;color:#fff;text-shadow:0 1px 2px rgba(0,0,0,.25)}
.q1{top:236px;height:87px;background:var(--panel-1)}
.q2{top:323px;height:81px;background:var(--panel-2)}
.q3{top:404px;height:81px;background:var(--panel-3)}
h2{position:absolute;font-weight:300;font-size:23px;color:#333;white-space:nowrap}
h2 em{font-style:normal;font-weight:400;color:var(--blue)}
.copy{position:absolute;font-size:10.5px;line-height:15.6px;color:#222}
.copy p{margin-bottom:8.6px}
.copy .tight{margin-bottom:1.6px}
.copy .name{color:var(--blue)}
.art{position:absolute}
.about-art{left:385px;top:516px;width:212px;height:119px;background:linear-gradient(135deg,#f3f3f3,#d6d8da)}
.team-art{left:383px;top:828px;width:212px;height:119px;background:linear-gradient(120deg,#bfc8d0,#eef0f2 55%,#c9c2b8)}
.login label{position:absolute;left:636px;font-size:10.5px}
.field{left:703px;width:172px;height:23px;border:1px solid #d4d4d4;border-radius:3px;background:#fff}
.check{left:638px;top:631px;width:10px;height:10px;border:1px solid #888}
.remember{left:654px;top:629px;font-size:10.5px;color:var(--blue)}
.btn{left:801px;top:620px;width:74px;height:25px;border-radius:13px;background:linear-gradient(#4fc0e6,#1f97cf);color:#fff;font-size:10.5px;font-weight:700;text-align:center;line-height:25px}
.small{position:absolute;font-size:10.5px}
.small a{color:var(--blue);text-decoration:none}
.testimonial{left:636px;top:768px;width:242px}
.viewall{left:636px;top:1059px;font-size:10.5px;display:flex;align-items:center;gap:6px}
.viewall i{width:11px;height:11px;border-radius:50%;background:#555;display:inline-block;position:relative}
.viewall i::after{content:"";position:absolute;left:4px;top:3px;border-left:4px solid #fff;border-top:2.5px solid transparent;border-bottom:2.5px solid transparent}
.foot{font-size:10.5px;color:#222}
.social-box{left:879px;top:1157px;width:22px;height:22px;border-radius:4px;background:linear-gradient(#e4e4e4,#b8b8b8)}
</style>
</head>
<body>
<div class="abs top-strip"></div>
<nav class="abs main-nav">
  <a class="current" href="#">HOME</a>
  <a style="left:195px" href="#">ABOUT VELMARONE</a>
  <span class="nav-sep" style="left:338px"></span>
  <a style="left:360px" href="#">NEWS &amp; EVENTS</a>
  <span class="nav-sep" style="left:504px"></span>
  <a style="left:539px" href="#">SUPPORTS</a>
  <span class="nav-sep" style="left:651px"></span>
  <a style="left:690px" href="#">CONTACT US</a>
</nav>
<div class="abs rss"></div>

<div class="abs brand">Velmarone</div>

<address class="abs contact" style="font-style:normal">
  <b>Velmarone</b><br>
  48 Harrowfield Lane,<br>
  London N7 2QD, United Kingdom<br>
  <span class="k">T:</span> +44 (0) 208 555 0142 <span class="k">F:</span> +44 (0) 208 555 0178
  <span class="gap"></span>
  Republic Of Ireland &nbsp;<span class="k">T:</span> +353 (0) 861 555 207
  <span class="gap"></span>
  Greece and Cyprus <span class="k">T:</span> +357 995 55318
</address>

<div class="abs content"></div>

<div class="abs hero-photo" role="img" aria-label="Photo of smiling clinicians in lab coats beside a microscope"></div>
<div class="abs replay">REPLAY</div>

<div class="abs quick q1"><div class="ico"></div><span>MyVelmarone</span></div>
<div class="abs quick q2"><div class="ico"></div><span>Request a Demo</span></div>
<div class="abs quick q3"><div class="ico"></div><span>News, blog feed</span></div>

<h2 style="left:84px;top:519px">About <em>Velmarone</em></h2>
<div class="art about-art" role="img" aria-label="Illustration of business people assembling giant puzzle pieces"></div>
<div class="copy" style="left:80px;top:556px;width:300px">
  <p>In today's changing environment, healthcare organisations globally are faced with conflicting challenges; to reduce costs while offering improved healthcare services to patients that expect better and better services.</p>
</div>
<div class="copy" style="left:80px;top:627px;width:500px">
  <p>Most health care organisations operate using either manual<br>paper based processed or a mix of different technologies and systems that have been developed over a long period of time, using proprietary, mainframe type architectures.</p>
  <p>There are also different stove-pipe systems used in many departments, each with different information on patients. This creates a big problem in how to develop new solutions to deliver efficient services in line with National and European Health care directives.</p>
  <p><span class="name">Velmarone</span> enables clients to transform the way they deliver and manage healthcare services by providing innovative solutions based on modern, intuitive, integrated and internet enabled technologies.</p>
</div>

<h2 style="left:84px;top:806px"><em>Velmarone</em> Healthcare</h2>
<div class="art team-art" role="img" aria-label="Photo of colleagues working together at a laptop"></div>
<div class="copy" style="left:82px;top:843px;width:290px">
  <p class="tight">&nbsp;Through our solutions, rich up-to-date patient centric information can be made accessible securely at the point of care, through wireless, mobile, internet or local area connections using the most appropriate access device (PC, laptop, Tablet PC, PDA, phone).</p>
  <p class="tight">Our approach aims to minimize risk and fully leverage existing investments. We acknowledge that hospitals are complex organizations so effective change cannot happen overnight.</p>
</div>
<div class="copy" style="left:82px;top:972px;width:500px">
  <p class="tight">We integrate existing investment in systems and we enable Healthcare providers to migrate from their current to their desired state in a gradual, phased and prioritized way.</p>
  <p style="margin-bottom:1.5px"><span class="name">Velmarone</span> solutions exploit opportunities offered by the latest technological advances. Our goal is to help:</p>
  <p style="margin:0;line-height:17.3px">• Reduce clinical errors<br>• Improve patient care<br>• Improve efficiency</p>
</div>

<h2 style="left:637px;top:519px">Customer <em style="font-weight:700">Login</em></h2>
<div class="login">
  <label style="top:565px">Username:</label>
  <label style="top:590px">Password:</label>
</div>
<div class="abs field" style="top:557px"></div>
<div class="abs field" style="top:588px"></div>
<div class="abs check"></div>
<div class="abs remember">Remember Me</div>
<div class="abs btn">Log In</div>
<div class="small" style="left:636px;top:650px">Forgot your password?</div>
<div class="small" style="left:636px;top:674px">No Account Yet? &nbsp;<a href="#">Create an Account now</a></div>

<h2 style="left:635px;top:732px">Testimonials</h2>
<div class="copy testimonial">
  <p>Bore vel ut la feugiat augait lortini amcore ver sequate issecte dolestrud tat landipit dolestrud tat adionsendip enim eugait delesse magna adiat. Ed del et, sequam enim alit prat wis nulputem dio et lobor sed do del duipit nis niscill uptat.</p>
  <p>Ustrud magna feuguer iustionullan utatem illam dolore ting ea feugue facidunt non hendreet, quis nulputpatie modolor augiamc onsequisi ero dunt et dolore magna facinismodio exero do consequam eumsan et dolobortie modolummodit verat praessi eliquatis et, con ut la autpat il eugait in verit, Ustrud magna feuguer iustionullan utatem illam dolore ting ea feugue facidunt non hendreet, quis nulputpatie modolor augiamc onsequisi ero dunt et dolore magna facinismodio exero do consequam</p>
  <p><span class="name">quissit, susci tie commoluptat. Elit do dolobor</span></p>
</div>
<div class="abs viewall"><i></i>View All</div>

<div class="abs foot" style="left:44px;top:1138px">Copyright © 2008 Velmarone Ltd</div>
<div class="abs foot" style="right:39px;top:1138px">Terms of Use</div>
<div class="abs foot" style="left:840px;top:1162px;color:#555">Chirper</div>
<div class="abs social-box"></div>
</body>
</html>
```